Brenley Mechanical Drain Cleaning and Jetting

We need to show our customers and potential customers that we now have the ability to perform Drain Cleaning, camera inspections, location services, and Hydro-Jetting Services. I would like the the colors to match the previous design.

```html
<!DOCTYPE html>
<html lang="en">
<head>
<meta charset="utf-8">
<title>Brenley Mechanical – Drain Cleaning and Jetting Flyers</title>
<link rel="stylesheet" href="https://fonts.googleapis.com/css2?family=Poppins:wght@400;500;600;700;800&family=Oswald:wght@500;700&display=swap">
<style>
:root{
  --green:#1f7a4d;
  --green-dark:#16603b;
  --gold:#c9a23a;
  --ink:#2b2b2b;
  --paper:#ffffff;
  --paper-soft:#f1f2f1;
  --stage:#e6e8e6;
  --photo-grey-a:#8a8c8b;
  --photo-grey-b:#4a4c4b;
}
*{box-sizing:border-box;margin:0;padding:0}
html,body{width:1200px;height:900px;overflow:hidden;background:var(--stage);font-family:"Poppins",sans-serif;color:var(--ink)}
.canvas{position:relative;width:1200px;height:900px}
.flyer{position:absolute;top:150px;width:440px;height:600px;background:var(--paper);overflow:hidden;box-shadow:0 6px 18px rgba(0,0,0,.15)}
.flyer--classic{left:120px}
.flyer--photo{left:640px;background:linear-gradient(180deg,var(--paper) 0%,var(--paper-soft) 100%)}

.brand{position:absolute;display:flex;align-items:center;gap:8px;font-weight:700;color:var(--green);font-size:17px;letter-spacing:.5px;text-transform:uppercase;line-height:1.1}
.brand__mark{width:14px;height:14px;background:var(--green);border-radius:50%;flex:none}

/* classic flyer */
.flyer--classic .brand{top:26px;right:28px}
.swoosh{position:absolute;left:0;top:60px}
.headline-band{position:absolute;left:0;top:112px;width:100%;height:104px;background:var(--green);display:flex;align-items:center;justify-content:center;text-align:center;color:#fff;font-weight:800;font-size:23px;line-height:1.25;text-transform:uppercase}
.gold-rule{position:absolute;left:0;width:100%;height:5px;background:var(--gold)}
.workshop-photo{position:absolute;left:0;top:221px;width:100%;height:200px;background:linear-gradient(135deg,var(--photo-grey-a),var(--photo-grey-b))}
.thumbs{position:absolute;left:28px;top:335px;display:flex;gap:18px}
.thumb{width:80px;height:80px;border-radius:12px;border:3px solid var(--green);background:linear-gradient(135deg,#bdbdbd,#6f6f6f)}
.thumb--pin{background:linear-gradient(135deg,#f3f3f3,#d8d8d8)}
.thumb--jet{background:linear-gradient(135deg,#9a8a86,#5e5351)}
.services-title{position:absolute;font-weight:800;color:var(--green);font-size:22px;text-transform:uppercase;letter-spacing:.3px;line-height:1.2}
.flyer--classic .services-title{left:28px;top:434px}
.service-list{position:absolute;list-style:none;font-size:13px;line-height:1.75}
.service-list li{display:flex;align-items:center;gap:7px}
.flyer--classic .service-list--a{left:28px;top:470px}
.flyer--classic .service-list--b{left:250px;top:430px}
.tick{width:12px;height:12px;flex:none}
.contact{position:absolute;left:28px;top:540px;font-size:12px;font-weight:500;line-height:1.6}
.contact li{list-style:none;display:flex;align-items:center;gap:7px}
.phone-icon{width:11px;height:11px;flex:none}
.web-bar{position:absolute;right:0;width:232px;height:40px;background:var(--green);color:#fff;font-size:12px;display:flex;align-items:center;gap:8px;padding-left:26px;white-space:nowrap;clip-path:polygon(14px 0,100% 0,100% 100%,0 100%)}
.flyer--classic .web-bar{top:492px}
.globe{width:12px;height:12px;flex:none}

/* photo flyer */
.hero-photo{position:absolute;left:0;top:0;width:270px;height:370px;border-bottom-right-radius:270px 250px;background:linear-gradient(160deg,#cbbfa8,#7e7a74 60%,#3f3f3f)}
.hero-arc{position:absolute;left:0;top:0}
.spot{position:absolute;width:88px;height:88px;border-radius:50%;border:5px solid var(--green);box-shadow:0 0 0 3px #fff}
.spot--jet{left:231px;top:61px;background:radial-gradient(circle,#b6a7a3,#6c5d5a)}
.spot--pin{left:196px;top:194px;background:radial-gradient(circle,#ffffff,#d6d6d6)}
.spot--camera{left:112px;top:282px;background:radial-gradient(circle,#c7c7c7,#6c6c6c)}
.flyer--photo .brand{top:160px;right:20px;font-size:15px}
.flyer--photo .services-title{right:20px;top:290px;font-size:19px}
.flyer--photo .service-list{right:20px;top:324px;text-align:right}
.flyer--photo .service-list li{justify-content:flex-end}
.offer-box{position:absolute;left:0;top:395px;width:260px;height:130px;background:var(--green);border-radius:0 22px 22px 0;padding:16px 10px 0 20px;color:#fff;display:block}
.offer-box__lead{display:block;font-size:18px;font-weight:500;line-height:1.2}
.offer-box__accent{display:block;color:var(--gold);font-size:16px;font-weight:600;text-transform:uppercase;line-height:1.35}
.offer-box__main{display:block;font-family:"Oswald",sans-serif;font-weight:700;font-size:26px;text-transform:uppercase;line-height:1.25;white-space:nowrap}
.flyer--photo .web-bar{top:532px}
.flyer--photo .contact{top:540px}
</style>
</head>
<body>
<main class="canvas">

  <article class="flyer flyer--classic">
    <svg class="swoosh" width="440" height="60" viewBox="0 0 440 60" aria-hidden="true">
      <path d="M0 52 C60 10 140 4 200 14 L0 14 Z" fill="var(--green)"/>
      <path d="M0 52 C80 14 150 10 210 16" fill="none" stroke="var(--green)" stroke-width="3"/>
    </svg>
    <div class="brand"><span class="brand__mark"></span>Brenley Mechanical</div>
    <div class="gold-rule" style="top:106px"></div>
    <h1 class="headline-band">Have you inspected<br>all your pluming fixtures</h1>
    <div class="gold-rule" style="top:216px"></div>
    <div class="workshop-photo" role="img" aria-label="Greyscale photo of plumbing tools and pipe fittings"></div>
    <div class="thumbs">
      <div class="thumb" role="img" aria-label="Plumber working under a sink"></div>
      <div class="thumb" role="img" aria-label="Technician running a drain camera"></div>
      <div class="thumb thumb--pin" role="img" aria-label="Red location pin on a map"></div>
      <div class="thumb thumb--jet" role="img" aria-label="Hydro-jetting nozzle spraying water"></div>
    </div>
    <h2 class="services-title">Our Services</h2>
    <ul class="service-list service-list--a">
      <li><svg class="tick" viewBox="0 0 12 12"><circle cx="6" cy="6" r="5.3" fill="none" stroke="var(--green)" stroke-width="1.2"/><path d="M3.4 6.2l1.8 1.7 3.4-3.6" fill="none" stroke="var(--green)" stroke-width="1.4"/></svg>Drain Cleaning</li>
      <li><svg class="tick" viewBox="0 0 12 12"><circle cx="6" cy="6" r="5.3" fill="none" stroke="var(--green)" stroke-width="1.2"/><path d="M3.4 6.2l1.8 1.7 3.4-3.6" fill="none" stroke="var(--green)" stroke-width="1.4"/></svg>Camera Inspections</li>
    </ul>
    <ul class="service-list service-list--b">
      <li><svg class="tick" viewBox="0 0 12 12"><circle cx="6" cy="6" r="5.3" fill="none" stroke="var(--green)" stroke-width="1.2"/><path d="M3.4 6.2l1.8 1.7 3.4-3.6" fill="none" stroke="var(--green)" stroke-width="1.4"/></svg>location services</li>
      <li><svg class="tick" viewBox="0 0 12 12"><circle cx="6" cy="6" r="5.3" fill="none" stroke="var(--green)" stroke-width="1.2"/><path d="M3.4 6.2l1.8 1.7 3.4-3.6" fill="none" stroke="var(--green)" stroke-width="1.4"/></svg>Hydro-Jetting</li>
    </ul>
    <div class="web-bar"><svg class="globe" viewBox="0 0 12 12"><circle cx="6" cy="6" r="5" fill="none" stroke="#fff"/><path d="M1 6h10M6 1c-2.5 3-2.5 7 0 10M6 1c2.5 3 2.5 7 0 10" fill="none" stroke="#fff" stroke-width=".8"/></svg>www.brenleymechanical.com</div>
    <ul class="contact">
      <li><svg class="phone-icon" viewBox="0 0 12 12"><path d="M2.5 1.2l2 .3.7 2.3-1.3 1a7 7 0 0 0 3.3 3.3l1-1.3 2.3.7.3 2a1 1 0 0 1-1 1A9.5 9.5 0 0 1 1.5 2.2a1 1 0 0 1 1-1z" fill="var(--green)"/></svg>1-800.GO.BRENLEY</li>
      <li><svg class="phone-icon" viewBox="0 0 12 12"><path d="M2.5 1.2l2 .3.7 2.3-1.3 1a7 7 0 0 0 3.3 3.3l1-1.3 2.3.7.3 2a1 1 0 0 1-1 1A9.5 9.5 0 0 1 1.5 2.2a1 1 0 0 1 1-1z" fill="var(--green)"/></svg>555-014-2290</li>
    </ul>
  </article>

  <article class="flyer flyer--photo">
    <div class="hero-photo" role="img" aria-label="Plumber in overalls repairing pipes under a kitchen sink"></div>
    <svg class="hero-arc" width="440" height="400" viewBox="0 0 440 400" aria-hidden="true">
      <path d="M273 0 L273 120 A273 253 0 0 1 0 373" fill="none" stroke="var(--gold)" stroke-width="3"/>
      <path d="M279 0 L279 120 A279 259 0 0 1 0 379" fill="none" stroke="var(--green)" stroke-width="4"/>
    </svg>
    <div class="spot spot--jet" role="img" aria-label="Hydro-jetting nozzle close-up"></div>
    <div class="spot spot--pin" role="img" aria-label="Red location pin"></div>
    <div class="spot spot--camera" role="img" aria-label="Technician with drain camera reel"></div>
    <div class="brand"><span class="brand__mark"></span><span>Brenley<br>Mechanical</span></div>
    <h2 class="services-title">Our Services</h2>
    <ul class="service-list">
      <li>Drain Cleaning<svg class="tick" viewBox="0 0 12 12"><circle cx="6" cy="6" r="5.3" fill="none" stroke="var(--green)" stroke-width="1.2"/><path d="M3.4 6.2l1.8 1.7 3.4-3.6" fill="none" stroke="var(--green)" stroke-width="1.4"/></svg></li>
      <li>Camera Inspections<svg class="tick" viewBox="0 0 12 12"><circle cx="6" cy="6" r="5.3" fill="none" stroke="var(--green)" stroke-width="1.2"/><path d="M3.4 6.2l1.8 1.7 3.4-3.6" fill="none" stroke="var(--green)" stroke-width="1.4"/></svg></li>
      <li>location services<svg class="tick" viewBox="0 0 12 12"><circle cx="6" cy="6" r="5.3" fill="none" stroke="var(--green)" stroke-width="1.2"/><path d="M3.4 6.2l1.8 1.7 3.4-3.6" fill="none" stroke="var(--green)" stroke-width="1.4"/></svg></li>
      <li>Hydro-Jetting<svg class="tick" viewBox="0 0 12 12"><circle cx="6" cy="6" r="5.3" fill="none" stroke="var(--green)" stroke-width="1.2"/><path d="M3.4 6.2l1.8 1.7 3.4-3.6" fill="none" stroke="var(--green)" stroke-width="1.4"/></svg></li>
    </ul>
    <h1 class="offer-box">
      <span class="offer-box__lead">Have You</span>
      <span class="offer-box__accent">Inspected all your</span>
      <span class="offer-box__main">Pluming Fixtures</span>
    </h1>
    <div class="web-bar"><svg class="globe" viewBox="0 0 12 12"><circle cx="6" cy="6" r="5" fill="none" stroke="#fff"/><path d="M1 6h10M6 1c-2.5 3-2.5 7 0 10M6 1c2.5 3 2.5 7 0 10" fill="none" stroke="#fff" stroke-width=".8"/></svg>www.brenleymechanical.com</div>
    <ul class="contact">
      <li><svg class="phone-icon" viewBox="0 0 12 12"><path d="M2.5 1.2l2 .3.7 2.3-1.3 1a7 7 0 0 0 3.3 3.3l1-1.3 2.3.7.3 2a1 1 0 0 1-1 1A9.5 9.5 0 0 1 1.5 2.2a1 1 0 0 1 1-1z" fill="var(--green)"/></svg>1-800.GO.BRENLEY</li>
      <li><svg class="phone-icon" viewBox="0 0 12 12"><path d="M2.5 1.2l2 .3.7 2.3-1.3 1a7 7 0 0 0 3.3 3.3l1-1.3 2.3.7.3 2a1 1 0 0 1-1 1A9.5 9.5 0 0 1 1.5 2.2a1 1 0 0 1 1-1z" fill="var(--green)"/></svg>555-014-2290</li>
    </ul>
  </article>

</main>
</body>
</html>
```